Willowmere Equine Sanctuary Flyer Urgent

Willowmere Equine Sanctuary

Rescue • Rehabilitation • Sanctuary

Willowmere Equine Sanctuary provides a safe and ethical refuge for horses, ponies and donkeys who have nowhere else to go. Some arrive needing rehabilitation and careful retraining, while others find permanent sanctuary here due to age, injury or behavioural needs.

Our mission is simple: to improve the physical and psychological wellbeing of every animal in our care.

At Willowmere we focus on:
• Rescue and rehabilitation of horses in need
• Lifetime sanctuary for those who cannot be rehomed
• Education and advocacy for responsible horse care
• Equine rehabilitation services to help horses recover and thrive

Sponsor a Horse

One of the most meaningful ways to support our work is by sponsoring one of our residents. Each horse, pony or donkey only has one sponsor!

Your sponsorship helps provide:
• Hay and feed
• Veterinary care
• Hoof trimming and routine health care
• Rugs, shelter and daily care

Many of our horses will live out their lives here, and sponsorship ensures they are safe, well fed and cared for every single day.

Sponsorship starts from $15 - $25 per week / $60 -$100 per month.

How You Can Help

• Sponsor a horse
• Make a donation
• Share our work with others

Your support helps us continue to say yes to horses who need a second chance.

📍 Willowmere Park, Victoria
📧 carla@willowmerepaddock.org

📞 0400 519 627

Font styles to use
Serif
Sans Serif

Colors
F0912C
F2A743
F7CA91
FBE8D2
FDF5EE
EE7325
F08F49
F5BC92
FAE3D3
FDF4ED

Requirements
Should not have
• Photos not provided by Willowmere

```html
<!DOCTYPE html>
<html lang="en">
<head>
<meta charset="utf-8">
<title>Willowmere Equine Sanctuary Flyer</title>
<link href="https://fonts.googleapis.com/css2?family=Anton&family=Outfit:wght@400;500;600;700&display=swap" rel="stylesheet">
<style>
  :root{
    --page-bg:#ecebe8;
    --paper:#f6f3ef;
    --maroon:#5a1f1f;
    --peach:#fccf9e;
    --peach-band:#edb07a;
    --orange:#f3a54a;
    --charcoal:#4a4a4a;
    --charcoal-deep:#3d3d3d;
    --white:#ffffff;
    --ink:#3a2a22;
  }
  *{box-sizing:border-box;margin:0;padding:0}
  html,body{width:1200px;height:856px;overflow:hidden}
  body{background:var(--page-bg);font-family:"Outfit",sans-serif;position:relative}
  .flyer{position:absolute;left:317px;top:28px;width:566px;height:800px;background:var(--paper);overflow:hidden;box-shadow:0 6px 24px rgba(0,0,0,.18)}
  .abs{position:absolute}
  .hero-photo{left:0;top:0;width:566px;height:354px;
    background:
      radial-gradient(ellipse at 30% 30%,rgba(176,92,40,.95),rgba(140,66,28,.0) 60%),
      radial-gradient(ellipse at 80% 60%,rgba(120,52,24,.95),rgba(120,52,24,0) 55%),
      linear-gradient(160deg,#5e6b3a 0%,#8c4a22 35%,#7a3a1c 65%,#4c4a2a 100%)}
  .hero-shade{left:0;top:150px;width:330px;height:204px;background:linear-gradient(90deg,rgba(40,25,15,.55),rgba(40,25,15,0))}
  .lower-photo{left:0;top:354px;width:566px;height:392px;background:linear-gradient(180deg,#eeeae5,#f4f1ed)}
  .brand{right:24px;top:21px;display:flex;align-items:center;gap:8px}
  .brand-name{font-weight:400;font-size:19px;color:var(--white);line-height:1;text-align:right}
  .brand-mark{width:40px;height:70px;background:var(--white)}
  .tagline{left:33px;top:186px;font-family:"Anton",sans-serif;font-size:17px;color:var(--white);letter-spacing:.1px}
  .intro{left:33px;top:213px;width:275px;font-size:10.8px;line-height:15.4px;color:var(--white)}
  .sponsor{left:31px;top:336px;width:283px;height:277px;background:var(--peach);color:var(--maroon)}
  .sponsor h2{font-family:"Anton",sans-serif;font-weight:400;font-size:18px;color:var(--maroon);margin:12px 0 0 18px}
  .sponsor p{font-size:11px;line-height:15.4px;margin:7px 12px 0 18px;color:#4a2718}
  .sponsor-band{background:var(--peach-band);margin-top:5px;padding:1px 12px 3px 18px;font-size:11px;line-height:14.5px;font-weight:500;color:var(--maroon)}
  .sponsor-band ul{list-style:none}
  .sponsor-band li::before{content:"• "}
  .help{left:31px;top:613px;width:283px;height:90px;background:linear-gradient(90deg,#3f3a36,#5b4d42 55%,#3b2f28);color:var(--white);padding:8px 0 0 18px}
  .help h2{font-family:"Anton",sans-serif;font-weight:400;font-size:16px;line-height:20px}
  .help ul{list-style:none;font-size:12.5px;line-height:18px;font-weight:500}
  .help li::before{content:"•";margin-right:8px}
  .mission-tab{left:325px;top:243px;width:118px;height:26px;background:var(--peach);font-family:"Anton",sans-serif;font-size:15px;color:var(--maroon);padding:3px 0 0 11px}
  .mission{left:325px;top:269px;width:214px;height:185px;background:var(--charcoal);padding:9px 0 0 13px;font-weight:700;font-size:24.5px;line-height:28px;color:var(--white)}
  .mission em{font-style:normal;color:var(--orange)}
  .animals-photo{left:325px;top:454px;width:214px;height:92px;background:linear-gradient(90deg,#7a6a4a,#9a7650 45%,#3e3426 70%,#6b6a3c)}
  .focus{left:325px;top:546px;width:214px;height:159px;background:var(--charcoal-deep);color:var(--white);padding:9px 8px 0 12px;font-size:10.8px;line-height:15.4px}
  .focus ul{list-style:none;margin-top:7px}
  .focus li{padding-left:9px;text-indent:-6px}
  .focus li::before{content:"• ";font-size:8px}
  .closing{left:0;width:566px;top:727px;text-align:center;font-size:12px;color:var(--ink)}
  .closing b{font-weight:700}
  .contact{left:0;top:750px;width:566px;height:25px;background:var(--maroon);color:var(--white);display:flex;justify-content:space-around;align-items:center;font-size:11px;padding:0 20px}
  .contact span{display:flex;align-items:center;gap:5px}
  .contact svg{width:11px;height:11px;fill:var(--white)}
</style>
</head>
<body>
  <article class="flyer">
    <div class="abs hero-photo" role="img" aria-label="Photograph of two chestnut horses nuzzling against a green bush background"></div>
    <div class="abs hero-shade"></div>
    <div class="abs lower-photo" role="img" aria-label="Faint washed-out photograph of a herd of horses"></div>

    <div class="abs brand">
      <div class="brand-name">Willowmere<br>Equine Sanctuary</div>
      <div class="brand-mark"></div>
    </div>

    <h1 class="abs tagline">RESCUE • REHABILITATION • SANCTUARY</h1>
    <p class="abs intro">Willowmere Equine Sanctuary provides a safe and ethical refuge for horses, ponies and donkeys who have nowhere else to go. Some arrive needing rehabilitation and careful retraining, while others find permanent sanctuary here due to age, injury or behavioural needs.</p>

    <section class="abs sponsor">
      <h2>SPONSOR A HORSE</h2>
      <p>One of the most meaningful ways to support our work is by sponsoring one of our residents. Each horse, pony or donkey only has one sponsor!</p>
      <div class="sponsor-band">
        Your sponsorship helps provide:
        <ul>
          <li>Hay and feed</li>
          <li>Veterinary care</li>
          <li>Hoof trimming and routine health care</li>
          <li>Rugs, shelter and daily care</li>
        </ul>
      </div>
      <p>Many of our horses will live out their lives here, and sponsorship ensures they are safe, well fed and cared for every single day.</p>
      <p>Sponsorship starts from $15 - $25 per week / $60 -$100 per month.</p>
    </section>

    <section class="abs help" role="group" aria-label="How you can help, over a photograph of ponies">
      <h2>HOW YOU CAN HELP</h2>
      <ul>
        <li>Sponsor a horse</li>
        <li>Make a donation</li>
        <li>Share our work with others</li>
      </ul>
    </section>

    <div class="abs mission-tab">OUR MISSION:</div>
    <p class="abs mission">To <em>improve</em> the <em>physical</em> and <em>psychological wellbeing</em> of <em>every animal</em> in our <em>care.</em></p>

    <div class="abs animals-photo" role="img" aria-label="Photograph of a young deer and a dog touching noses"></div>

    <section class="abs focus">
      At Willowmere we focus on:
      <ul>
        <li>Rescue and rehabilitation of horses in need</li>
        <li>Lifetime sanctuary for those who cannot be rehomed</li>
        <li>Education and advocacy for responsible horse care</li>
        <li>Equine rehabilitation services to help horses recover and thrive</li>
      </ul>
    </section>

    <p class="abs closing">Your support helps us continue to say <b>YES</b> to horses who need a second chance.</p>

    <footer class="abs contact">
      <span><svg viewBox="0 0 24 24"><path d="M12 2a7 7 0 0 0-7 7c0 5 7 13 7 13s7-8 7-13a7 7 0 0 0-7-7zm0 9.5A2.5 2.5 0 1 1 12 6.5a2.5 2.5 0 0 1 0 5z"/></svg>Willowmere Park, Victoria</span>
      <span><svg viewBox="0 0 24 24"><path d="M2 5h20v14H2z" fill="none" stroke="#fff" stroke-width="2"/><path d="M2 5l10 8 10-8" fill="none" stroke="#fff" stroke-width="2"/></svg>carla@willowmerepaddock.org</span>
      <span><svg viewBox="0 0 24 24"><path d="M6.6 10.8a15 15 0 0 0 6.6 6.6l2.2-2.2a1 1 0 0 1 1-.25 11.4 11.4 0 0 0 3.6.57 1 1 0 0 1 1 1V20a1 1 0 0 1-1 1A17 17 0 0 1 3 4a1 1 0 0 1 1-1h3.5a1 1 0 0 1 1 1c0 1.25.2 2.45.57 3.57a1 1 0 0 1-.25 1z"/></svg>0400 519 627</span>
    </footer>
  </article>
</body>
</html>
```